"The Craft of Patron Care," fourth edition cover design

Later this year, my publisher, Harold Penmarsh & Daughters, will issue a fourth, substantially revised edition of "The Craft of Patron Care," following the 2016 publication of the third edition and the second and first versions that were issued earlier.

To distinguish this new edition from previous ones, I need a cover design that visually connects and is consistent with what has preceded it, while signaling this is a new and different, worthy of prospective readers/buyers’ attention.

Attached are three different verbal approaches to the new cover; these are NOT MEANT to serve as actual designs, but rather will give you a sense of how language is to be deployed:

The first emphasizes “ART” as the key visual word in the book title;
The second emphasizes “CLIENT SERVICE” as the key visual words in the book title; and,
The third emphasizes just the word "CLIENT" in the book title.

A top-of-the-page is a pre-head that applies to all three versions:
“6 TIMELESS PRINCIPLES FOR ADVERTISING & MARKETING PRO’s
IN AN AI WORLD"

There's a mid-page sub-head for all three versions:
“THE CLASSIC GUIDE,” followed by
“FOURTH EDITION BY GERALD ASHCOMBE

And there's a one-line, bottom-of-the-page designation:
“Foreword by Mae Dunford, Global Executive Creative Director, Starbolt"

The pallette for the previously published third edition was black with red as an accent color on a field of white; I've attached a sample for reference, so you can see how it was executed. For this new fourth edition, I'd like to change the accent color from red to either Wedgewood blue, or British racing green, or an alternative that is assertive and color saturated -- think of primary colors -- that contrast sufficiently with the base of black. As an alternative, you can consider a cover that used either Wedgewood blue, British racing green, or another possibility as a full-bleed field, with copy content either revered out or surprinted.

Lastly, while the new cover largely is meant to be typographically driven, if you can come up with a visual metaphor that illustrates and builds on the book's title, that would be very helpful. By way of reference, the third edition's book cover attempted to do this by introducing a visual element at the end of the book's title that's meant to represent an artist's paint splatter (although I admit it didn't work as well as it should).

Target Market(s)

Prospective purchasers of the book who might discover copies at a bookstore, but more likely will encounter it through online distributors such as Riverdex, Hartwell & Pike, and Tindall’s.

Industry/Entity Type

Advertising and marketing

Font styles to use
Serif
Sans Serif
Other font styles liked:
• A mix of serif and san-serif typefaces is okay. for the examples I shared, I relieid on "Arial Rounded Bold" but you need not be weeded to this. If you opt to mix in a serif font, I am partial to Cambria as a typeface.

Requirements
Must have
• To achieve the goal of being “connected with but distinct” from previous editions, the new cover should be:  Largely typographic, but displaying a color palette different from the previous editions’ black-plus-red-accent on a canvas of white.  Any new accent color selected for use should be vibrant, strong, and highly saturated; think “British racing green,” “Wedgewood blue,” or their equivalents.  In addition to a powerful, “billboard” approach to type and color, consider other visual metaphors that are likely to engage the readers. The winning cover design will stand out from other books, while connecting with the previously published third edition.
Nice to have
• If you can find way to illustrate the book's title through a visual metaphor, that would be ideal.a
Should not have
• Anything that is frivolous or non-sensical

```html
<!DOCTYPE html>
<html lang="en">
<head>
<meta charset="utf-8">
<title>The Craft of Patron Care — Fourth Edition</title>
<link rel="stylesheet" href="https://fonts.googleapis.com/css2?family=Arimo:wght@700&family=Montserrat:wght@500;600;700;800&display=swap">
<style>
  :root {
    --backdrop: #000000;
    --paper: #ffffff;
    --ink: #000000;
    --accent: #3d69b2;
  }
  html, body {
    margin: 0;
    padding: 0;
    width: 1200px;
    height: 1200px;
    overflow: hidden;
    background: var(--backdrop);
  }
  .stage {
    position: relative;
    width: 1200px;
    height: 1200px;
  }
  .book-cover {
    position: absolute;
    left: 240px;
    top: 60px;
    width: 720px;
    height: 1080px;
    background: var(--paper);
  }
  .book-cover svg { display: block; width: 100%; height: 100%; }
  .sans-label { font-family: "Arimo", Arial, sans-serif; font-weight: 700; }
  .display { font-family: "Montserrat", "Helvetica Neue", sans-serif; }
  .ink { fill: var(--ink); }
  .accent { fill: var(--accent); }
  .title-top { font-weight: 600; font-size: 101px; }
  .title-key { font-weight: 800; font-size: 170px; }
  .title-end { font-weight: 800; font-size: 146px; }
  .classic { font-weight: 600; font-size: 54px; }
  .edition { font-weight: 600; font-size: 44px; }
  .prehead { font-size: 20px; }
  .prehead-accent { font-size: 26px; }
  .author { font-size: 42px; }
  .foreword { font-size: 20px; }
</style>
</head>
<body>
<main class="stage">
  <section class="book-cover" aria-label="Front cover: The Craft of Patron Care, fourth edition">
    <svg viewBox="0 0 720 1080" xmlns="http://www.w3.org/2000/svg">
      <g class="pre-head sans-label">
        <text class="prehead ink" x="47" y="64" textLength="628" lengthAdjust="spacingAndGlyphs">6 TIMELESS PRINCIPLES FOR ADVERTISING &amp; MARKETING PROS IN</text>
        <text class="prehead-accent accent" x="360" y="91" text-anchor="middle">AN  A.I. WORLD</text>
      </g>

      <g class="book-title display">
        <text class="title-top ink" x="49" y="302" textLength="625" lengthAdjust="spacingAndGlyphs">THE CRAFT OF</text>
        <text class="title-key accent" x="45" y="439" textLength="630" lengthAdjust="spacingAndGlyphs">PATRON</text>
        <text class="title-end ink" x="46" y="557" textLength="628" lengthAdjust="spacing">CARE</text>
      </g>

      <g class="sub-head display">
        <text class="classic ink" x="360" y="703" text-anchor="middle" textLength="574" lengthAdjust="spacingAndGlyphs">THE CLASSIC GUIDE</text>
        <text class="edition accent" x="360" y="755" text-anchor="middle" textLength="361" lengthAdjust="spacingAndGlyphs">FOURTH EDITION</text>
      </g>

      <g class="credits sans-label">
        <text class="author accent" x="675" y="1003" text-anchor="end">GERALD ASHCOMBE</text>
        <text class="foreword ink" x="675" y="1031" text-anchor="end" textLength="628" lengthAdjust="spacingAndGlyphs">Foreword by Mae Dunford, Global Executive Creative Director, Starbolt</text>
      </g>
    </svg>
  </section>
</main>
</body>
</html>
```